Political Marketing Company - Valentine's Day Card - Huge!

We need a 5"x7" Valentine's Day card in the style of the attached images. We want it to be slightly cartoon-y, but heartfelt. Copy for card is as follows, with direction:Outside: My love for you is…(Text only, bold san-serif font, light background)Inside: HUUUUUUUGE! (graphic of Harold Benning with hands out spanning both inside pages with “HUUUUUUUUGE!” above Benning, big, bold san serif font).

Font styles to use
Serif

```html
<!DOCTYPE html>
<html lang="en">
<head>
<meta charset="utf-8">
<title>Valentine's Card – Huge Love</title>
<link rel="stylesheet" href="https://fonts.googleapis.com/css2?family=Oswald:wght@700&family=Archivo+Black&display=swap">
<style>
  :root {
    --backdrop: #f6dcdc;
    --card-pink: #de5d7e;
    --card-pink-light: #e58a9d;
    --cream: #f2ebdf;
    --inside-cream: #ede4d9;
    --fold-shade: #d9d0c6;
    --heading-pink: #d9506f;
    --heart-line: #e0607f;
    --navy: #27266b;
    --skin: #df7a58;
    --suit: #2b2a5e;
  }
  html, body {
    margin: 0;
    padding: 0;
    width: 1200px;
    height: 1200px;
    overflow: hidden;
    background: var(--backdrop);
  }
  .canvas {
    position: relative;
    width: 1200px;
    height: 1200px;
  }
  .card {
    position: absolute;
    width: 760px;
    height: 520px;
    box-shadow: 0 6px 18px rgba(120, 60, 70, 0.25);
  }
  .card svg { display: block; width: 100%; height: 100%; }
  .card--outside { left: 110px; top: 70px; }
  .card--inside { left: 330px; top: 620px; }
  .cover-text {
    font-family: "Oswald", "Arial Narrow", sans-serif;
    font-weight: 700;
    font-size: 38px;
    fill: var(--heading-pink);
  }
  .huge-text {
    font-family: "Archivo Black", "Arial Black", sans-serif;
    font-size: 66px;
    fill: #ffffff;
    stroke: var(--navy);
    stroke-width: 2.5;
    paint-order: stroke;
    letter-spacing: 2px;
  }
  .heart-outline { fill: none; stroke-width: 2.2; stroke-linecap: round; stroke-linejoin: round; }
  .heart-outline--cream { stroke: var(--cream); }
  .heart-outline--pink { stroke: var(--heart-line); }
</style>
</head>
<body>
<main class="canvas">

  <!-- Outside spread -->
  <section class="card card--outside" aria-label="Card outside">
    <svg viewBox="0 0 760 520" xmlns="http://www.w3.org/2000/svg">
      <defs>
        <path id="heart" d="M12 21 C5 15 1 11 1 7 A5.5 5.5 0 0 1 12 5 A5.5 5.5 0 0 1 23 7 C23 11 19 15 12 21 Z"/>
        <linearGradient id="back-sheen" x1="0" y1="0" x2="1" y2="1">
          <stop offset="0" stop-color="#dd5c7d"/>
          <stop offset="0.7" stop-color="#e58a9d"/>
          <stop offset="1" stop-color="#df6a86"/>
        </linearGradient>
      </defs>
      <rect class="back-panel" x="0" y="0" width="380" height="520" fill="url(#back-sheen)"/>
      <rect class="front-panel" x="380" y="0" width="380" height="520" fill="var(--card-pink)"/>
      <line x1="380" y1="0" x2="380" y2="520" stroke="#c94e6d" stroke-width="1"/>

      <use href="#heart" class="heart-outline heart-outline--cream" transform="translate(165 235) scale(2.4)"/>

      <use href="#heart" fill="var(--cream)" transform="translate(415 95) scale(13)"/>
      <text class="cover-text" x="571" y="212" text-anchor="middle">MY LOVE</text>
      <text class="cover-text" x="571" y="254" text-anchor="middle">FOR YOU IS...</text>

      <use href="#heart" class="heart-outline heart-outline--cream" transform="translate(420 40) scale(1.6)"/>
      <use href="#heart" class="heart-outline heart-outline--cream" transform="translate(520 30) scale(1.7)"/>
      <use href="#heart" class="heart-outline heart-outline--cream" transform="translate(650 30) scale(1.8)"/>
      <use href="#heart" class="heart-outline heart-outline--cream" transform="translate(690 370) scale(1.5)"/>
      <use href="#heart" class="heart-outline heart-outline--cream" transform="translate(700 420) scale(1.4)"/>
      <use href="#heart" class="heart-outline heart-outline--cream" transform="translate(460 440) scale(1.5)"/>
      <use href="#heart" class="heart-outline heart-outline--cream" transform="translate(600 470) scale(1.3)"/>
    </svg>
  </section>

  <!-- Inside spread -->
  <section class="card card--inside" aria-label="Card inside">
    <svg viewBox="0 0 760 520" xmlns="http://www.w3.org/2000/svg">
      <defs>
        <path id="heart-in" d="M12 21 C5 15 1 11 1 7 A5.5 5.5 0 0 1 12 5 A5.5 5.5 0 0 1 23 7 C23 11 19 15 12 21 Z"/>
        <linearGradient id="fold" x1="0" y1="0" x2="1" y2="0">
          <stop offset="0" stop-color="var(--inside-cream)"/>
          <stop offset="0.44" stop-color="var(--inside-cream)"/>
          <stop offset="0.5" stop-color="var(--fold-shade)"/>
          <stop offset="0.56" stop-color="var(--inside-cream)"/>
          <stop offset="1" stop-color="var(--inside-cream)"/>
        </linearGradient>
        <linearGradient id="figure-tone" x1="0" y1="0" x2="0" y2="1">
          <stop offset="0" stop-color="#e8c07a"/>
          <stop offset="0.25" stop-color="var(--skin)"/>
          <stop offset="0.6" stop-color="var(--suit)"/>
          <stop offset="1" stop-color="var(--suit)"/>
        </linearGradient>
        <path id="huge-arc" d="M60 270 Q395 80 730 270"/>
      </defs>
      <rect x="0" y="0" width="760" height="520" fill="url(#fold)"/>

      <use href="#heart-in" class="heart-outline heart-outline--pink" transform="translate(130 40) scale(1.3)"/>
      <use href="#heart-in" class="heart-outline heart-outline--pink" transform="translate(670 90) scale(1.4)"/>
      <use href="#heart-in" class="heart-outline heart-outline--pink" transform="translate(100 180) scale(2.3)"/>
      <use href="#heart-in" class="heart-outline heart-outline--pink" transform="translate(95 250) scale(1.7)"/>
      <use href="#heart-in" class="heart-outline heart-outline--pink" transform="translate(630 230) scale(1.5)"/>
      <use href="#heart-in" class="heart-outline heart-outline--pink" transform="translate(640 300) scale(2.4)"/>

      <rect role="img" aria-label="Cartoon illustration of Harold Benning in a navy suit and red tie, eyes closed, hands spread wide across both inside pages"
            x="180" y="130" width="430" height="390" rx="20" fill="url(#figure-tone)"/>

      <text class="huge-text">
        <textPath href="#huge-arc" startOffset="50%" text-anchor="middle">HUUUUUUUUGE!</textPath>
      </text>
    </svg>
  </section>

</main>
</body>
</html>
```